business card - for laser marking

I need design (curve) for my business card (make with laser) size 85mm x 55mm. How it look business card with laser marking see attached picture.

color:
Background: white
text and icons black

Please include: one side
1. dominik vrhovec - direktor
2. phone: +386(0)41 726 193
+386(0)592 817 06
3. info@zlatorez.example
4. faecebook.com/Zlatorez.Ex
5. KP-ATELJE, Dominik Vrhovec s.p.
Brezova ulica 17, 1000 Ljubljana, SI
6. logo

Please include: second side
1. logo
2. www.zlatorez.example
3. Lasersko graviranje
ovitki telefonov, ohišja telefonov / tablic, nakit, ure, alu vizitke, dog-tagi, kemični svinčniki, orodja, noži, vžigalniki

Industry/Entity Type

Business

Contact Information for Business Card

Please include: one side
+386(0)592 817 06
3. info@zlatorez.example
6. logo

1. logo
2. www.zlatorez.example
3. Lasersko graviranje

Colors
000000
ffffff

Requirements
Must have
• I need design (curve) for my business card (make with laser) size 85mm x 55mm. How it look business card with laser marking see attached picture.
• color:
• Background: white
• text and icons black
• Please include: one side
• 1. dominik vrhovec - direktor
• 2. phone: +386(0)41 726 193
• +386(0)592 817 06
• 3. info@zlatorez.example
• 4. faecebook.com/Zlatorez.Ex
• 5. KP-ATELJE, Dominik Vrhovec s.p.
• Brezova ulica 17, 1000 Ljubljana, SI
• 6. logo
• Please include: second side
• 1. logo
• 2. www.zlatorez.example
• 3. Lasersko graviranje
• ovitki telefonov, ohišja telefonov / tablic, nakit, ure, alu vizitke, dog-tagi, kemični svinčniki, orodja, noži, vžigalniki

```html
<!DOCTYPE html>
<html lang="sl">
<head>
<meta charset="utf-8">
<title>ZLATOREZ – vizitka</title>
<link rel="stylesheet" href="https://fonts.googleapis.com/css2?family=Roboto+Condensed:wght@400;700&family=Roboto:wght@400;700&display=swap">
<style>
  :root{
    --bg:#ecebe8;
    --card:#ffffff;
    --magenta:#d3164f;
    --green:#5d9e35;
    --ink:#3a3a3a;
    --paper-shadow:rgba(0,0,0,.18);
  }
  *{margin:0;padding:0;box-sizing:border-box}
  html,body{width:1200px;height:911px;overflow:hidden;background:var(--bg)}
  .stage{position:relative;width:1200px;height:911px}
  .card{
    position:absolute;width:560px;height:362px;border-radius:22px;
    background:var(--card);overflow:hidden;
    box-shadow:0 6px 18px var(--paper-shadow);
  }
  .card--front{left:25px;top:250px}
  .card--back{left:615px;top:300px}

  /* front */
  .front-art{position:absolute;inset:0}
  .holder{position:absolute;right:260px;top:38px;text-align:right;
    font-family:"Roboto Condensed",sans-serif}
  .holder__name{color:var(--magenta);font-weight:700;font-size:23px;letter-spacing:.3px}
  .holder__role{color:var(--green);font-weight:700;font-size:13px;letter-spacing:.6px;margin-top:2px}
  .contacts{position:absolute;right:26px;top:34px;list-style:none;
    font-family:"Roboto Condensed",sans-serif;color:#fff;font-size:14px}
  .contacts li{display:flex;justify-content:flex-end;align-items:center;gap:8px;height:19px}
  .contacts svg{width:13px;height:13px;flex:none}
  .address{position:absolute;left:232px;bottom:34px;
    font-family:"Roboto Condensed",sans-serif;color:#fff;font-size:14px;line-height:19px}
  .brand-front{position:absolute;left:42px;top:230px;display:flex;align-items:center;gap:10px}
  .brand-front__dot{width:22px;height:22px;border-radius:50%;background:var(--green)}
  .brand-front__name{font-family:"Roboto Condensed",sans-serif;font-weight:700;
    font-size:30px;color:var(--magenta);letter-spacing:1px}

  /* back */
  .back-decor{position:absolute;left:0;top:40px;width:330px;height:300px;
    background:radial-gradient(ellipse at 45% 45%,rgba(211,22,79,.14),rgba(93,158,53,.10) 55%,rgba(255,255,255,0) 75%)}
  .back-content{position:absolute;left:58px;top:70px;font-family:"Roboto",sans-serif}
  .brand-back{font-family:"Roboto Condensed",sans-serif;font-weight:700;font-size:50px;
    color:var(--magenta);letter-spacing:2px;line-height:1}
  .service-title{margin-top:26px;font-size:14px;color:var(--ink)}
  .service-list{margin-top:6px;font-size:13px;line-height:19px;color:var(--ink);width:440px}
  .website{margin-top:24px;font-weight:700;font-size:15px;color:var(--magenta)}
</style>
</head>
<body>
<main class="stage">

  <section class="card card--front" aria-label="Sprednja stran vizitke">
    <svg class="front-art" viewBox="0 0 560 362" width="560" height="362" aria-hidden="true">
      <path d="M338,0 C306,120 262,170 226,262 C210,305 196,338 186,362" fill="none" stroke="var(--green)" stroke-width="5"/>
      <path d="M350,0 C318,120 274,170 238,262 C222,305 208,338 198,362 L560,362 L560,0 Z" fill="var(--magenta)"/>
    </svg>

    <div class="holder">
      <div class="holder__name">DOMINIK VRHOVEC</div>
      <div class="holder__role">DIREKTOR</div>
    </div>

    <ul class="contacts">
      <li>+386(0)592 817 06
        <svg viewBox="0 0 16 16"><path d="M4 1l3 3-2 2c1 2 3 4 5 5l2-2 3 3-2 3C7 15 1 9 1 3z" fill="#fff"/></svg></li>
      <li>+386(0)41 726 193
        <svg viewBox="0 0 16 16"><rect x="4" y="1" width="8" height="14" rx="1.5" fill="none" stroke="#fff" stroke-width="1.6"/></svg></li>
      <li>info@zlatorez.example
        <svg viewBox="0 0 16 16"><rect x="1" y="3" width="14" height="10" fill="#fff"/><path d="M1 3l7 6 7-6" fill="none" stroke="var(--magenta)" stroke-width="1.4"/></svg></li>
      <li>Zlatorez.Ex
        <svg viewBox="0 0 16 16"><rect x="1" y="1" width="14" height="14" rx="2" fill="#fff"/></svg></li>
    </ul>

    <div class="address">
      KP-ATELJE, Dominik Vrhovec s.p.<br>
      Brezova ulica 17, 1000 Ljubljana, SI
    </div>

    <div class="brand-front">
      <span class="brand-front__dot"></span>
      <span class="brand-front__name">ZLATOREZ</span>
    </div>
  </section>

  <section class="card card--back" aria-label="Zadnja stran vizitke">
    <div class="back-decor" role="img" aria-label="Blag barvni madež v roza in zelenih tonih kot ozadje"></div>
    <div class="back-content">
      <div class="brand-back">ZLATOREZ</div>
      <p class="service-title">Lasersko graviranje</p>
      <p class="service-list">ovitki telefonov, ohišja telefonov / tablic, nakit, ure, alu vizitke, dog-tagi, kemični svinčniki, orodja, noži, vžigalniki</p>
      <p class="website">www.zlatorez.example</p>
    </div>
  </section>

</main>
</body>
</html>
```